Valiant Sons Ministry - 3

Features of prayer:
- Prayer should be out of a filial relationship with the Father. Heb. 5:7
- Prayer is a divine responsibility to walk and work with God. Col. 1:10, 1 Cor. 15:58
- Prayer should depend on the Holy Spirit: Rom. 8:26-27, Jude 1:20
- Prayer should be effective and fervent: James 5:16, Luke 22:44
- Prayer should be word based: Acts 4:23-33
- Prayer should demonstrate faith: Matt. 21:22
- Prayer should proceed from a heart of worship: Phil. 4:6
- Time is of essence in prayer: Luke 6:12
- Prayer requires you as a whole: Acts 6:4, Rom. 12:1
- You learn how to pray by praying: Luke 11:2

You learn how to pray by praying
"Men ought always to pray and not to faint"

Join the Valiant Sons Ministry!

Ministry

```html
<!DOCTYPE html>
<html lang="en">
<head>
<meta charset="utf-8">
<title>Valiant Sons Ministry</title>
<link rel="stylesheet" href="https://fonts.googleapis.com/css2?family=Tinos:ital,wght@0,400;0,700;1,700&display=swap">
<style>
  :root {
    --paper: #ffffff;
    --title-blue: #1b5c98;
    --ink: #111111;
    --join-green: #5a9a2b;
    --ring-navy: #1d2f63;
    --ring-green: #6aa84f;
    --ring-core: #d9ecd0;
    --brand-blue: #1f5f95;
    --brand-dot: #3b8fc4;
    --sky-deep: #2a1a10;
    --sky-amber: #e98a2a;
    --sky-gold: #f6c25a;
  }
  * { margin: 0; padding: 0; box-sizing: border-box; }
  html, body { width: 1200px; height: 1080px; overflow: hidden; background: var(--paper); }
  .poster {
    position: relative;
    width: 1200px;
    height: 1080px;
    background: var(--paper);
    font-family: "Tinos", "Times New Roman", serif;
    color: var(--ink);
    overflow: hidden;
  }
  .sunset-photo {
    position: absolute;
    left: 0;
    top: 712px;
    width: 1200px;
    height: 368px;
    background:
      linear-gradient(to bottom, var(--paper) 0%, rgba(255,255,255,0) 26%),
      radial-gradient(ellipse 38% 50% at 50% 62%, var(--sky-gold) 0%, var(--sky-amber) 45%, rgba(233,138,42,0) 100%),
      linear-gradient(to bottom, #c9a07a 0%, #b0622a 45%, var(--sky-deep) 100%);
  }
  .brand {
    position: absolute;
    top: 14px;
    left: 318px;
    display: flex;
    align-items: center;
    gap: 20px;
  }
  .brand-mark {
    width: 100px;
    height: 100px;
    border-radius: 50%;
    background: var(--brand-dot);
  }
  .brand-name {
    font-size: 32px;
    font-weight: 400;
    color: var(--brand-blue);
    line-height: 1.1;
    width: 420px;
  }
  .ministry-title {
    position: absolute;
    top: 126px;
    left: 0;
    width: 1200px;
    text-align: center;
    font-size: 53px;
    line-height: 64px;
    font-weight: 700;
    color: var(--title-blue);
    letter-spacing: 1px;
  }
  .features {
    position: absolute;
    top: 204px;
    left: 42px;
    width: 1130px;
  }
  .features-heading {
    font-size: 26px;
    line-height: 36px;
    font-weight: 700;
    color: var(--title-blue);
    margin-left: 62px;
    margin-bottom: 4px;
  }
  .feature-list { list-style: none; }
  .feature-item {
    display: flex;
    align-items: center;
    gap: 24px;
    font-size: 22px;
    line-height: 31px;
    font-weight: 700;
    white-space: nowrap;
  }
  .feature-item .ring { flex: 0 0 38px; width: 38px; height: 24px; }
  .motto {
    position: absolute;
    top: 572px;
    left: 0;
    width: 1200px;
    text-align: center;
    font-size: 41px;
    line-height: 48px;
    font-weight: 700;
  }
  .quote {
    position: absolute;
    top: 624px;
    left: 0;
    width: 1200px;
    text-align: center;
    font-size: 26px;
    line-height: 32px;
    font-weight: 700;
    font-style: italic;
  }
  .invite {
    position: absolute;
    top: 660px;
    left: 0;
    width: 1200px;
    text-align: center;
    font-size: 34px;
    line-height: 42px;
    font-weight: 700;
    color: var(--join-green);
  }
</style>
</head>
<body>
<main class="poster">
  <div class="sunset-photo" role="img" aria-label="Photo of a glowing orange sunset sky with the silhouette of a man raising both arms in praise"></div>

  <header class="brand">
    <div class="brand-mark"></div>
    <div class="brand-name">Hearts of Praise Global Fellowship</div>
  </header>

  <h1 class="ministry-title">VALIANT SONS MINISTRY (VSM)</h1>

  <section class="features">
    <h2 class="features-heading">Features of prayer:</h2>
    <ul class="feature-list">
      <li class="feature-item"><svg class="ring" viewBox="0 0 38 24"><ellipse cx="19" cy="12" rx="17" ry="10.5" fill="var(--ring-navy)"/><ellipse cx="19" cy="12" rx="12" ry="7" fill="var(--ring-green)"/><ellipse cx="19" cy="12" rx="8" ry="4.5" fill="var(--ring-core)"/></svg>Prayer should be out of a filial relationship with the Father. Heb. 5:7</li>
      <li class="feature-item"><svg class="ring" viewBox="0 0 38 24"><ellipse cx="19" cy="12" rx="17" ry="10.5" fill="var(--ring-navy)"/><ellipse cx="19" cy="12" rx="12" ry="7" fill="var(--ring-green)"/><ellipse cx="19" cy="12" rx="8" ry="4.5" fill="var(--ring-core)"/></svg>Prayer is a divine responsibility to walk and work with God. Col. 1:10, 1 Cor. 15:58</li>
      <li class="feature-item"><svg class="ring" viewBox="0 0 38 24"><ellipse cx="19" cy="12" rx="17" ry="10.5" fill="var(--ring-navy)"/><ellipse cx="19" cy="12" rx="12" ry="7" fill="var(--ring-green)"/><ellipse cx="19" cy="12" rx="8" ry="4.5" fill="var(--ring-core)"/></svg>Prayer should depend on the Holy Spirit: Rom. 8:26-27, Jude 1:20</li>
      <li class="feature-item"><svg class="ring" viewBox="0 0 38 24"><ellipse cx="19" cy="12" rx="17" ry="10.5" fill="var(--ring-navy)"/><ellipse cx="19" cy="12" rx="12" ry="7" fill="var(--ring-green)"/><ellipse cx="19" cy="12" rx="8" ry="4.5" fill="var(--ring-core)"/></svg>Prayer should be effective and fervent: James 5:16, Luke 22:44</li>
      <li class="feature-item"><svg class="ring" viewBox="0 0 38 24"><ellipse cx="19" cy="12" rx="17" ry="10.5" fill="var(--ring-navy)"/><ellipse cx="19" cy="12" rx="12" ry="7" fill="var(--ring-green)"/><ellipse cx="19" cy="12" rx="8" ry="4.5" fill="var(--ring-core)"/></svg>Prayer should be word based: Acts 4:23-33</li>
      <li class="feature-item"><svg class="ring" viewBox="0 0 38 24"><ellipse cx="19" cy="12" rx="17" ry="10.5" fill="var(--ring-navy)"/><ellipse cx="19" cy="12" rx="12" ry="7" fill="var(--ring-green)"/><ellipse cx="19" cy="12" rx="8" ry="4.5" fill="var(--ring-core)"/></svg>Prayer should demonstrate faith: Matt. 21:22</li>
      <li class="feature-item"><svg class="ring" viewBox="0 0 38 24"><ellipse cx="19" cy="12" rx="17" ry="10.5" fill="var(--ring-navy)"/><ellipse cx="19" cy="12" rx="12" ry="7" fill="var(--ring-green)"/><ellipse cx="19" cy="12" rx="8" ry="4.5" fill="var(--ring-core)"/></svg>Prayer should proceed from a heart of worship: Phil. 4:6</li>
      <li class="feature-item"><svg class="ring" viewBox="0 0 38 24"><ellipse cx="19" cy="12" rx="17" ry="10.5" fill="var(--ring-navy)"/><ellipse cx="19" cy="12" rx="12" ry="7" fill="var(--ring-green)"/><ellipse cx="19" cy="12" rx="8" ry="4.5" fill="var(--ring-core)"/></svg>Time is of essence in prayer: Luke 6:12</li>
      <li class="feature-item"><svg class="ring" viewBox="0 0 38 24"><ellipse cx="19" cy="12" rx="17" ry="10.5" fill="var(--ring-navy)"/><ellipse cx="19" cy="12" rx="12" ry="7" fill="var(--ring-green)"/><ellipse cx="19" cy="12" rx="8" ry="4.5" fill="var(--ring-core)"/></svg>Prayer requires you as a whole: Acts 6:4, Rom. 12:1</li>
      <li class="feature-item"><svg class="ring" viewBox="0 0 38 24"><ellipse cx="19" cy="12" rx="17" ry="10.5" fill="var(--ring-navy)"/><ellipse cx="19" cy="12" rx="12" ry="7" fill="var(--ring-green)"/><ellipse cx="19" cy="12" rx="8" ry="4.5" fill="var(--ring-core)"/></svg>You learn how to pray by praying: Luke 11:2</li>
    </ul>
  </section>

  <p class="motto">YOU LEARN HOW TO PRAY BY PRAYING</p>
  <p class="quote">“Men ought always to pray and not to faint”</p>
  <p class="invite">JOIN THE VALIANT SONS MINISTRY!</p>
</main>
</body>
</html>
```